MerriTide. Sunless Tanning Mousse Label

I'm looking for a label creation for a new brand of sunless tanning solutions. They are in 6.7oz bottles (template attached).

For the front of the bottle (see template) I would like an abstract multi coloured design taking up just over half the top of the bottle (approx 60%) and going around the design (this is similar to the design inspiration attached). I would this design to use the attached colour palette of pinks. It can be swirls, drips, squares, lines, whatever you think will look good.

The logo will then be over top of that abstract design in the upper 1/3, in the colour #3fe0d0

Under the abstract design the following text:

Cedar Hush (Larger text)
Amber Core (2nd heading)
1 Hour Sunless Mousse (Sub text)
The No Orange Guarantee! (Sub text)
Vegan Formula (sub text)

The sub texts for above can be fun, have coloured background, different fonts, whatever looks good and is sill fun.

Towards the bottom of the front of bottle we require the sizing information:

200ml 6.7 Fl Oz

On the left side of the front (so in the template the middle smaller section) I would like the phrase "You ain't gotta get ready if you stay ready" Could you please make this as a separate little quote, with a fun design to it. It's like a little hidden gem on the side of the bottle.

On the back of the bottle for now can you please start towards the top with:

Cedar Hush Mousse (larger)
Amber core (second heading)
Deep Mediterranean Inspired Tan (second heading)
Easy to Apply & Streak Free
Vegan friendly & 100% natural DHA tan actives

Under this I require approx 1.5" of Lorem Ipsum for now which will take the place of directions for using the product.

Under that in small writing can we include "Warning: This product does not contain a sunscreen and will not protect against sunburn. For external use only. If skin irritation occurs, discontinue use. Carry out a patch test 24 hours prior to full body use. Store below 25(degrees sign)C."

At the bottom is the smallest yet still legible writing, can we include the ingredients that are listed below.

Target Market(s)

Females 24-35 who take care of themselves and always want to look good. It's a youthful fun product.

Requirements
Must have
• Bright colours, and just screams FUN and youthful.

Ingredients must be listed on the back. They dont' need to take up more than an inch in height, less if possible.
*******************************************

INGREDIENTS: Water (Aqua), Propylene Glycol, Dihydroxyacetone, Peg-6 Caprylic/Capric Glycerides, Dihydroxypropyl Peg-5 Linoleammonium Chloride, Peg-7 Glyceryl Cocoate, Caramel,
Phenoxyethanol, Caprylyl Glycol, Potassium Sorbate, Hexylene Glycol, Glycerin, Helianthus Annuus (Sunflower) Seed Oil, Beta Vulgaris (Beet) Root Extract, Panthenol, Solanum Lycopersicum
(Tomato) Fruit Extract, Vaccinium Macrocarpon (Cranberry) Fruit Extract, L-ascorbic Acid (Vitamin C), Tocopheryl Acetate (Vitamin E), Theobroma Cacao (Cocoa) Seed Butter, Rosa Canina (Rose Hip)
Fruit Oil, Glycine Soja (Soybean) Oil, Cucumis Sativus (Cucumber) Fruit Extract, Blue 1 (CI 42090), Red 40 (CI 16035), Yellow 6 (CI 15985), Green 5 (CI 61570), Yellow 5 (CI 19140), Red 33 (CI 17200)

*****************************
Nice to have
• Several options to choose from, some can include a gradient into geometric shapes, rather than solid colour. Experiment
Should not have
• Do not want it to look medical.
Want colours to stay in the same pink family for the abstract design - can use white also.

```html
<!DOCTYPE html>
<html lang="en">
<head>
<meta charset="utf-8">
<title>MerriTide – Cedar Hush Mousse Label</title>
<link rel="stylesheet" href="https://fonts.googleapis.com/css2?family=Poppins:wght@400;500;600;700;800&family=Dancing+Script:wght@500&display=swap">
<style>
:root{
  --pink:#ec1d8c;
  --pink-deep:#c4208f;
  --pink-light:#f58cc4;
  --violet:#9a1f7c;
  --teal:#3fe0d0;
  --hot:#e3196d;
  --ink:#1a1a1a;
  --paper:#ffffff;
  --bg:#f4f4f4;
}
*{box-sizing:border-box;margin:0;padding:0}
html,body{width:800px;height:1200px;overflow:hidden;background:var(--bg);font-family:"Poppins",sans-serif}
.label{position:absolute;left:38px;top:299px;width:725px;height:602px;background:var(--paper);overflow:hidden;box-shadow:0 4px 18px rgba(0,0,0,.12)}
.marble{position:absolute;left:0;top:0;width:725px;height:440px}
.abs{position:absolute}
.center{text-align:center}
.back{left:0;width:310px}
.back-title{top:30px;font-weight:800;font-size:24px;color:var(--paper);letter-spacing:.5px}
.back-mousse{top:58px;font-weight:500;font-size:22px;color:var(--teal);letter-spacing:6px}
.back-base{top:96px;font-weight:700;font-size:11px;color:var(--paper);letter-spacing:3px;display:flex;justify-content:center;align-items:center;gap:6px}
.back-base::before,.back-base::after{content:"";width:16px;height:2px;background:var(--paper)}
.back-inspired{top:130px;font-weight:700;font-size:12px;line-height:16px;color:var(--teal);text-transform:uppercase}
.back-claims{top:176px;font-size:10px;line-height:12px;color:var(--paper)}
.back-claims strong{font-weight:600}
.back-directions{top:249px;left:60px;width:190px;font-size:10px;line-height:12.5px;color:var(--paper)}
.warning-head{top:412px;font-size:7px;font-weight:500;color:var(--hot);display:flex;justify-content:center;align-items:center;gap:3px}
.warning-text{top:426px;left:58px;width:196px;font-size:7.5px;line-height:9.5px;color:var(--ink)}
.ingredients{top:490px;left:50px;width:212px;font-size:4.6px;line-height:5.7px;color:var(--ink)}
.ingredients strong{font-weight:700}
.quote{left:334px;top:250px;transform:translate(-50%,-50%) rotate(-90deg);width:260px;font-family:"Dancing Script",cursive;font-size:21px;line-height:22px;color:var(--paper);text-align:center;white-space:nowrap}
.brand{left:408px;top:38px;font-weight:500;font-size:26px;color:var(--teal);letter-spacing:.5px}
.front-title{left:404px;top:222px;font-weight:800;font-size:58px;line-height:56px;color:var(--paper);letter-spacing:-1px}
.front-base{left:407px;top:440px;font-weight:700;font-size:25px;color:var(--violet)}
.front-sub{left:407px;top:478px;display:flex;font-size:13px;font-weight:500}
.front-sub .tag{background:var(--pink);color:var(--paper);padding:1px 4px;border:1px solid var(--pink-deep)}
.front-sub .tag b{font-weight:700}
.front-sub .plain{color:var(--pink);padding:1px 4px}
.guarantee{left:407px;top:513px;font-weight:700;font-size:11px;color:var(--hot)}
.vegan{left:407px;top:539px;font-size:10.5px;color:var(--teal);display:flex;align-items:center;gap:2px}
.size{left:604px;top:562px;font-size:10px;font-weight:600;color:var(--hot);text-align:right;line-height:10px}
.size small{display:block;font-size:6px;font-weight:500;color:var(--ink)}
</style>
</head>
<body>
<section class="label">
  <svg class="marble" viewBox="0 0 725 440" role="img" aria-label="Abstract pink and violet marbled swirl artwork with dripping lower edge">
    <defs>
      <linearGradient id="swirl" x1="0" y1="0" x2="1" y2="1">
        <stop offset="0" stop-color="#f0409b"/>
        <stop offset=".35" stop-color="#c4208f"/>
        <stop offset=".6" stop-color="#f58cc4"/>
        <stop offset=".8" stop-color="#ec1d8c"/>
        <stop offset="1" stop-color="#b12a9a"/>
      </linearGradient>
    </defs>
    <path fill="url(#swirl)" d="M0 0H725V350C718 372 700 400 690 388C680 378 682 340 664 346C640 352 648 392 620 386C596 380 606 338 580 342C552 346 560 388 530 390C500 392 510 350 480 352C452 354 448 378 420 372C392 366 398 340 368 340C336 340 338 372 306 370C278 368 270 340 240 345C210 350 212 380 180 376C152 372 150 340 122 344C100 348 108 396 80 400C52 404 62 352 40 350C18 348 22 410 0 426Z"/>
  </svg>

  <div class="abs back center back-title">CEDAR HUSH</div>
  <div class="abs back center back-mousse">MOUSSE</div>
  <div class="abs back back-base">AMBER CORE</div>
  <div class="abs back center back-inspired">Deep Mediterranean<br>Inspired Tan</div>
  <p class="abs back center back-claims"><strong>Easy to Apply &amp; Streak Free</strong><br>Vegan friendly &amp; 100% natural<br>DHA tan actives</p>
  <p class="abs center back-directions">Lorem ipsum dolor sit amet, consectetuer adipiscing elit, sed diam nonummy nibh euismod tincidunt ut laoreet dolore magna aliquam erat volutpat. Ut wisi enim ad minim veniam,</p>

  <div class="abs back warning-head">
    <svg width="10" height="9" viewBox="0 0 10 9" aria-hidden="true"><path d="M5 .6L9.4 8.4H.6Z" fill="none" stroke="currentColor" stroke-width=".9"/><path d="M5 3.3V5.8M5 6.6V7.2" stroke="currentColor" stroke-width=".9"/></svg>
    WARNING
  </div>
  <p class="abs center warning-text">This product does not contain a sunscreen and will not protect against sunburn. For external use only. If skin irritation occurs, discontinue use. Carry out a patch test 24 hours prior to full body use. Store below 25ºC.</p>
  <p class="abs center ingredients"><strong>INGREDIENTS:</strong> Water (Aqua), Propylene Glycol, Dihydroxyacetone, Peg-6 Caprylic/Capric Glycerides, Dihydroxypropyl Peg-5 Linoleammonium Chloride, Peg-7 Glyceryl Cocoate, Caramel, Phenoxyethanol, Caprylyl Glycol, Potassium Sorbate, Hexylene Glycol, Glycerin, Helianthus Annuus (Sunflower) Seed Oil, Beta Vulgaris (Beet) Root Extract, Panthenol, Solanum Lycopersicum (Tomato) Fruit Extract, Vaccinium Macrocarpon (Cranberry) Fruit Extract, L-ascorbic Acid (Vitamin C), Tocopheryl Acetate (Vitamin E), Theobroma Cacao (Cocoa) Seed Butter, Rosa Canina (Rose Hip) Fruit Oil, Glycine Soja (Soybean) Oil, Cucumis Sativus (Cucumber) Fruit Extract, Blue 1 (CI 42090), Red 40 (CI 16035), Yellow 6 (CI 15985), Green 5 (CI 61570), Yellow 5 (CI 19140), Red 33 (CI 17200)</p>

  <p class="abs quote">You ain't gotta get ready<br>if you stay ready</p>

  <div class="abs brand">MerriTide</div>
  <h1 class="abs front-title">CEDAR<br>HUSH</h1>
  <h2 class="abs front-base">AMBER CORE</h2>
  <div class="abs front-sub"><span class="tag"><b>1 Hour</b> Sunless</span><span class="plain">Mousse</span></div>
  <div class="abs guarantee">THE NO ORANGE GUARANTEE!</div>
  <div class="abs vegan">
    <svg width="11" height="10" viewBox="0 0 11 10" aria-hidden="true"><path d="M1 9C1 4 4 1 10 1C10 6 7 9 1 9Z" fill="currentColor"/><path d="M1 9L7 4" stroke="#fff" stroke-width=".8"/></svg>
    Vegan Formula
  </div>
  <div class="abs size">200ml<small>6.7 Fl Oz</small></div>
</section>
</body>
</html>
```